Killer design for artists website and gallery

Current website is www.plumvista.com.au and it runs on a very simple Wordpress standard theme. We would like a theme designed and customised to suit the branding and style. We have someone who will then code the site in HTML and CSS into Wordpress.

The general theme and branding can be seen on the site at the moment. Please note I have now uploaded full size files into the project. The website background files are for reference only as they are currently on the site. There is no requirement to use them in the new design, however the logo must be as per the attachment.. Please submit a home page/main gallery, and we will request additional pages (about us, other galleries etc.) from those designers we like during the project time.
Updates

Please note I have now uploaded full size files into the project. The website background files are for reference only as they are currently on the site. There is no requirement to use them in the new design, however the logo must be as per the attachment.

Target Market(s)

sales are only in Australia, and priced between approx $100 and $1000. Most viewers and buyers are 20-40 years old, and looking for a casual canvas work for home, or a gift.

Industry/Entity Type

Artists

Font styles to use
Serif
Sans Serif

Requirements
Must have
• gallery of images, responsive design, ability to select categories of pictures (see top menu on current site) and have the gallery change to match, colours to match branding and logo.
Nice to have
• simple minimalist style is preferred. More like http://www.tobiasmerrow.com/ than http://www.cobaltloomstudio.com.au/ or http://www.velvetharbour.com.au/
Should not have
• does not need any online store, or shopping cart etc.

```html
<!DOCTYPE html>
<html lang="en">
<head>
<meta charset="utf-8">
<title>Plum Vista – Blog</title>
<link rel="stylesheet" href="https://fonts.googleapis.com/css2?family=Lato:wght@300;400;700&family=Roboto+Slab:wght@300;400&display=swap">
<style>
:root{
  --panel:#e4e3d6;
  --ink:#3b3b3b;
  --muted:#8a8a84;
  --line:#c9c8bb;
  --teal:#1d8a8c;
  --yellow:#e8e21a;
  --olive:#8c8620;
  --star:#e8a11a;
  --side-text:#d9d9d0;
  --dark:#151412;
}
*{box-sizing:border-box;margin:0;padding:0}
html,body{width:690px;height:1200px;overflow:hidden}
body{position:relative;font-family:'Lato',sans-serif;color:var(--ink);background:var(--dark)}
.backdrop-left{position:absolute;left:0;top:0;width:234px;height:1200px;
  background:linear-gradient(100deg,#0d0c0b 0%,#1c1a15 40%,#2e2a20 75%,#3a3426 100%)}
.backdrop-right{position:absolute;left:618px;top:0;width:72px;height:1200px;
  background:linear-gradient(180deg,#8a7a4e 0%,#a89a68 25%,#756a44 50%,#8f8458 75%,#6e6440 100%)}

/* sidebar */
.sidebar{position:absolute;left:0;top:0;width:234px;height:1200px;color:var(--side-text)}
.logo{position:absolute;left:96px;top:21px;width:89px;height:89px;border:1px solid #6d6a1c;border-radius:6px;background:#050505;
  display:flex;align-items:flex-end;justify-content:center;padding-bottom:14px}
.logo span{font-size:13px;font-weight:400;color:#f2f2f2;letter-spacing:.3px}
.tagline{position:absolute;left:70px;top:113px;width:140px;text-align:center;font-size:9.6px;line-height:12px;color:#fff}
.round-btn{position:absolute;top:151px;width:16px;height:16px;border:1px solid #bdbdb4;border-radius:50%;display:flex;align-items:center;justify-content:center}
.nav{position:absolute;left:71px;top:188px;list-style:none}
.nav li,.cats li{height:19.7px;font-size:6.5px;display:flex;align-items:center}
.nav li::before,.cats li::before{content:"›";color:var(--yellow);font-size:8px;width:11px}
.nav li.active{color:var(--yellow)}
.side-head{position:absolute;left:71px;width:138px;font-size:8.8px;font-weight:700;color:#fff}
.side-rule{position:absolute;left:71px;width:138px;height:1px;background:#8a8678}
.side-rule::before{content:"";position:absolute;left:0;top:-2px;width:5px;height:5px;border-radius:50%;background:var(--yellow)}
.side-rule::after{content:"";position:absolute;left:0;top:0;width:28px;height:1px;background:var(--yellow)}
.thumb{position:absolute;width:64px;height:44px;border-radius:2px}
.cats{position:absolute;left:71px;top:516px;width:138px;list-style:none}
.cats li{justify-content:flex-start;position:relative}
.cats .count{position:absolute;right:0;width:14px;height:14px;border:1px solid #9a978a;border-radius:50%;font-size:6px;display:flex;align-items:center;justify-content:center}
.archive{position:absolute;font-size:6.5px}
.archive.small{font-size:5.8px}
.tags{position:absolute;left:71px;top:859px;width:140px;display:flex;flex-wrap:wrap;gap:5px 3px}
.tag{font-size:5.6px;border:1px solid #b0ad9f;border-radius:2px;padding:1px 4px;line-height:7px}
.like-box{position:absolute;left:71px;top:910px;width:138px;height:205px;background:var(--olive)}
.like-logo{position:absolute;left:50px;top:14px;width:38px;height:38px;background:#080808;border-radius:3px;display:flex;align-items:flex-end;justify-content:center;padding-bottom:6px}
.like-logo span{font-size:6px;color:#eee}
.like-count{position:absolute;left:0;top:65px;width:138px;text-align:center;font-size:7.2px;color:#fff}
.like-btn{position:absolute;left:40px;top:80px;width:59px;height:17px;background:#4a4712;color:#fff;font-size:7px;display:flex;align-items:center;justify-content:center;gap:4px}
.fans{position:absolute;left:21px;top:113px;width:97px;height:73px;background:linear-gradient(135deg,#7a6a58,#a08a70 40%,#5a5a60 70%,#8a7a66)}
.social{position:absolute;top:1138px;width:16px;height:16px;border:1px solid #bdbdb4;border-radius:50%}
.copyright{position:absolute;left:60px;top:1170px;width:160px;text-align:center;font-size:6.5px;line-height:12px;color:#bdbdb4}

/* main panel */
.panel{position:absolute;left:234px;top:0;width:384px;height:1200px;background:var(--panel)}
.post{position:absolute;left:24px;width:336px;height:346px}
.post-title{position:absolute;left:0;top:0;font-family:'Roboto Slab',serif;font-weight:300;font-size:14.6px;color:#2f2f2f;white-space:nowrap}
.meta{position:absolute;left:0;top:27px;display:flex;gap:0;font-size:6.2px;color:var(--muted)}
.meta-item{display:flex;align-items:center;gap:4px;margin-right:17px}
.meta-icon{width:14px;height:14px;border:1px solid #b3b2a7;border-radius:50%;display:flex;align-items:center;justify-content:center}
.post-image{position:absolute;left:0;top:57px;width:336px;height:142px;border-radius:2px}
.stars{position:absolute;left:0;top:207px;display:flex;gap:6.6px}
.excerpt{position:absolute;left:0;top:226px;width:336px;font-size:7.3px;line-height:12px;color:#555}
.read-more{position:absolute;left:0;top:287px;width:63px;height:18px;border:1px solid #8c8b82;border-radius:2px;font-size:6.8px;display:flex;align-items:center;justify-content:center;color:#333}
.share{position:absolute;right:0;top:291px;display:flex;align-items:center;gap:5px;font-size:6.5px;color:#555}
.share-btn{height:12px;border:1px solid #bdbcb0;border-radius:2px;display:flex;align-items:center;gap:5px;padding:0 5px 0 2px;font-size:6.2px;color:#777}
.share-btn i{width:8px;height:8px;border-radius:1px;display:block}
.divider{position:absolute;left:0;top:320px;width:336px;height:1px;background:var(--line)}
.divider::before{content:"";position:absolute;left:0;top:-1px;width:50px;height:2px;background:var(--teal)}
.divider::after{content:"";position:absolute;left:-1px;top:-2px;width:5px;height:5px;border-radius:50%;background:var(--teal)}
.pager{position:absolute;left:24px;top:1047px;display:flex;gap:4px}
.pager span{width:14px;height:14px;border:1px solid #9c9b90;border-radius:2px;font-size:6.5px;display:flex;align-items:center;justify-content:center}
.pager .next{width:18px;background:var(--teal);border-color:var(--teal)}
.widget-title{position:absolute;top:1087px;font-size:11px;font-weight:400;color:#555}
.follow-text{position:absolute;left:24px;top:1105px;width:160px;font-size:6.4px;line-height:9.6px;color:#666}
.email-input{position:absolute;left:24px;top:1133px;width:154px;height:17px;border:1px solid #b6b5aa;background:#ecebe0;font-size:6.4px;color:#999;padding-left:8px;display:flex;align-items:center}
.follow-btn{position:absolute;left:24px;top:1155px;width:49px;height:15px;background:var(--teal);color:#fff;font-size:6.6px;font-weight:700;display:flex;align-items:center;justify-content:center}
.feed-arrow{position:absolute;top:1090px;width:10px;height:10px;background:var(--teal);border-radius:1px;display:flex;align-items:center;justify-content:center}
.feed-circle{position:absolute;left:200px;top:1108px;width:44px;height:44px;border-radius:50%;background:#2aa7de;border:2px solid #d9f0fa}
.feed-box{position:absolute;left:252px;top:1109px;width:107px;height:43px;border:1px solid #bdbcb0;border-radius:3px;font-size:6.2px;line-height:8.5px;color:#666;padding:7px 8px 0 10px}
.feed-box a{color:#2aa7de;text-decoration:none}
.feed-author{position:absolute;left:310px;top:1158px;display:flex;align-items:center;gap:4px;font-size:6px;font-weight:700;color:#888}
.feed-author i{width:12px;height:12px;border-radius:50%;background:#2aa7de;display:block}
</style>
</head>
<body>
<div class="backdrop-left" role="img" aria-label="Dark weathered timber texture"></div>
<div class="backdrop-right" role="img" aria-label="Soft painted sky and sailing ship backdrop"></div>

<aside class="sidebar">
  <div class="logo"><span>Plum Vista</span></div>
  <p class="tagline">Beautiful canvas art made in Melbourne</p>
  <div class="round-btn" style="left:120px">
    <svg width="8" height="8" viewBox="0 0 10 10"><path d="M1 5L5 1.5 9 5M2.5 4v5h2V6.5h1V9h2V4" fill="none" stroke="#ddd" stroke-width="1"/></svg>
  </div>
  <div class="round-btn" style="left:144px">
    <svg width="8" height="8" viewBox="0 0 10 10"><circle cx="4.2" cy="4.2" r="3" fill="none" stroke="#ddd" stroke-width="1.2"/><path d="M6.5 6.5L9 9" stroke="#ddd" stroke-width="1.2"/></svg>
  </div>
  <ul class="nav">
    <li class="active">Home</li><li>About</li><li>Cityscapes</li><li>Other Works</li><li>Seascapes</li><li>Testimonials</li><li>Works for Sale</li>
  </ul>

  <h3 class="side-head" style="top:337px">Recent Posts</h3>
  <div class="side-rule" style="top:354px"></div>
  <div class="thumb" style="left:71px;top:372px;background:linear-gradient(135deg,#c86040,#3a5a90 50%,#e8d0a0)" role="img" aria-label="Recent post: gallery exhibition"></div>
  <div class="thumb" style="left:146px;top:372px;background:linear-gradient(180deg,#2c6a70,#5a9a90 50%,#d8a070)" role="img" aria-label="Recent post: umbrella seascape"></div>
  <div class="thumb" style="left:71px;top:426px;background:linear-gradient(160deg,#5a6ab0,#d09050 60%,#6070b0)" role="img" aria-label="Recent post: golden tree landscape"></div>
  <div class="thumb" style="left:146px;top:426px;background:linear-gradient(180deg,#4a5a70,#2a90b0 50%,#3a4a5a)" role="img" aria-label="Recent post: figure in the rain"></div>

  <h3 class="side-head" style="top:490px">Categories</h3>
  <div class="side-rule" style="top:506px"></div>
  <ul class="cats">
    <li>Art<span class="count">8</span></li>
    <li>Cityscapes<span class="count">10</span></li>
    <li>Market<span class="count">3</span></li>
    <li>Other Work<span class="count">15</span></li>
    <li>Seascapes<span class="count">2</span></li>
    <li>Social<span class="count">6</span></li>
    <li>Wedding<span class="count">20</span></li>
    <li>Work In Progress<span class="count">5</span></li>
  </ul>

  <h3 class="side-head" style="top:692px">Blog Archives</h3>
  <div class="side-rule" style="top:708px"></div>
  <span class="archive" style="left:71px;top:719px">▾&nbsp;&nbsp;&nbsp;2014</span>
  <span class="archive" style="left:84px;top:735px">▾&nbsp;&nbsp;&nbsp;January</span>
  <span class="archive small" style="left:97px;top:750px">Into The Rain</span>
  <span class="archive small" style="left:97px;top:760px">Wood &amp; Trees</span>
  <span class="archive" style="left:71px;top:780px">›&nbsp;&nbsp;&nbsp;2013</span>
  <span class="archive" style="left:71px;top:795px">›&nbsp;&nbsp;&nbsp;2012</span>

  <h3 class="side-head" style="top:829px">Meta Tags</h3>
  <div class="side-rule" style="top:846px"></div>
  <div class="tags"><span class="tag">wedding</span><span class="tag">others</span><span class="tag">cityscapes</span><span class="tag">art</span><span class="tag">work in progress</span></div>

  <div class="like-box">
    <div class="like-logo"><span>Plum Vista</span></div>
    <p class="like-count">77 People like Plum Vista</p>
    <div class="like-btn">
      <svg width="8" height="8" viewBox="0 0 10 10"><path d="M1 4.5h2V9H1zM3 4.5L5 1c1 0 1.2.8 1 1.8L5.7 4H9l-.8 5H3" fill="none" stroke="#fff" stroke-width=".9"/></svg>Like Me
    </div>
    <div class="fans" role="img" aria-label="Grid of supporter profile photos"></div>
  </div>

  <div class="social" style="left:112px"></div>
  <div class="social" style="left:132px"></div>
  <div class="social" style="left:152px"></div>
  <p class="copyright">Copyright © 2014<br>All Rights Reserved to Plum Vista</p>
</aside>

<main class="panel">
  <article class="post" style="top:20px">
    <h2 class="post-title">My Newest Seascape</h2>
    <div class="meta">
      <span class="meta-item"><span class="meta-icon"><svg width="7" height="7" viewBox="0 0 10 10"><rect x="1" y="2" width="8" height="7" fill="none" stroke="#999"/><path d="M1 4.5h8" stroke="#999"/></svg></span>3<sup>rd</sup>&nbsp;February 2014</span>
      <span class="meta-item"><span class="meta-icon"><svg width="7" height="7" viewBox="0 0 10 10"><ellipse cx="5" cy="4.5" rx="4" ry="3" fill="#999"/><path d="M3 7l-1 2 3-2" fill="#999"/></svg></span>1 comment</span>
      <span class="meta-item"><span class="meta-icon"><svg width="7" height="7" viewBox="0 0 10 10"><path d="M5 9L1.2 5A2.2 2.2 0 015 2.2 2.2 2.2 0 018.8 5z" fill="#999"/></svg></span>5 Likes</span>
    </div>
    <div class="post-image" style="background:linear-gradient(180deg,#1e5a5e 0%,#2f7a78 35%,#8fb8a8 55%,#d4a070 75%,#d88a50 100%)" role="img" aria-label="Painting of a figure with a striped umbrella on the beach"></div>
    <div class="stars">
      <svg width="10" height="10" viewBox="0 0 10 10"><path d="M5 .5l1.4 3 3.1.3-2.4 2.1.7 3.1L5 7.4 2.2 9l.7-3.1L.5 3.8l3.1-.3z" fill="#e8a11a"/></svg>
      <svg width="10" height="10" viewBox="0 0 10 10"><path d="M5 .5l1.4 3 3.1.3-2.4 2.1.7 3.1L5 7.4 2.2 9l.7-3.1L.5 3.8l3.1-.3z" fill="#e8a11a"/></svg>
      <svg width="10" height="10" viewBox="0 0 10 10"><path d="M5 .5l1.4 3 3.1.3-2.4 2.1.7 3.1L5 7.4 2.2 9l.7-3.1L.5 3.8l3.1-.3z" fill="#e8a11a"/></svg>
      <svg width="10" height="10" viewBox="0 0 10 10"><path d="M5 .5l1.4 3 3.1.3-2.4 2.1.7 3.1L5 7.4 2.2 9l.7-3.1L.5 3.8l3.1-.3z" fill="none" stroke="#999" stroke-width=".7"/></svg>
      <svg width="10" height="10" viewBox="0 0 10 10"><path d="M5 .5l1.4 3 3.1.3-2.4 2.1.7 3.1L5 7.4 2.2 9l.7-3.1L.5 3.8l3.1-.3z" fill="none" stroke="#999" stroke-width=".7"/></svg>
    </div>
    <p class="excerpt">Lorem Ipsum is simply dummy text of the printing and typesetting industry. Lorem Ipsum has been the industry's standard dummy text ever since the 1500s, when an unknown printer took a galley of type and scrambled it to make a type specimen book. It has survived not only five centuries, but also the leap into electronic typesetting, remaining essentially unchanged...</p>
    <span class="read-more">READ MORE</span>
    <div class="share">Share this :
      <span class="share-btn"><i style="background:#3b5998"></i>Friendly</span>
      <span class="share-btn"><i style="background:#2aa7de"></i>Chirper</span>
      <span class="share-btn"><i style="background:#d34836"></i>Searchly</span>
    </div>
    <div class="divider"></div>
  </article>

  <article class="post" style="top:366px">
    <h2 class="post-title">My New style with Wood Highlighting</h2>
    <div class="meta">
      <span class="meta-item"><span class="meta-icon"><svg width="7" height="7" viewBox="0 0 10 10"><rect x="1" y="2" width="8" height="7" fill="none" stroke="#999"/><path d="M1 4.5h8" stroke="#999"/></svg></span>1<sup>st</sup>&nbsp;February 2014</span>
      <span class="meta-item"><span class="meta-icon"><svg width="7" height="7" viewBox="0 0 10 10"><ellipse cx="5" cy="4.5" rx="4" ry="3" fill="#999"/><path d="M3 7l-1 2 3-2" fill="#999"/></svg></span>10 comment</span>
      <span class="meta-item"><span class="meta-icon"><svg width="7" height="7" viewBox="0 0 10 10"><path d="M5 9L1.2 5A2.2 2.2 0 015 2.2 2.2 2.2 0 018.8 5z" fill="#999"/></svg></span>22 Likes</span>
    </div>
    <div class="post-image" style="background:linear-gradient(180deg,#2a4a9a 0%,#3a5cb0 25%,#6a78a8 45%,#8a8aa0 58%,#c88a4a 72%,#b87038 100%)" role="img" aria-label="Painting of a row of colourful beach huts"></div>
    <div class="stars">
      <svg width="10" height="10" viewBox="0 0 10 10"><path d="M5 .5l1.4 3 3.1.3-2.4 2.1.7 3.1L5 7.4 2.2 9l.7-3.1L.5 3.8l3.1-.3z" fill="#e8a11a"/></svg>
      <svg width="10" height="10" viewBox="0 0 10 10"><path d="M5 .5l1.4 3 3.1.3-2.4 2.1.7 3.1L5 7.4 2.2 9l.7-3.1L.5 3.8l3.1-.3z" fill="#e8a11a"/></svg>
      <svg width="10" height="10" viewBox="0 0 10 10"><path d="M5 .5l1.4 3 3.1.3-2.4 2.1.7 3.1L5 7.4 2.2 9l.7-3.1L.5 3.8l3.1-.3z" fill="#e8a11a"/></svg>
      <svg width="10" height="10" viewBox="0 0 10 10"><path d="M5 .5l1.4 3 3.1.3-2.4 2.1.7 3.1L5 7.4 2.2 9l.7-3.1L.5 3.8l3.1-.3z" fill="none" stroke="#999" stroke-width=".7"/></svg>
      <svg width="10" height="10" viewBox="0 0 10 10"><path d="M5 .5l1.4 3 3.1.3-2.4 2.1.7 3.1L5 7.4 2.2 9l.7-3.1L.5 3.8l3.1-.3z" fill="none" stroke="#999" stroke-width=".7"/></svg>
    </div>
    <p class="excerpt">Lorem Ipsum is simply dummy text of the printing and typesetting industry. Lorem Ipsum has been the industry's standard dummy text ever since the 1500s, when an unknown printer took a galley of type and scrambled it to make a type specimen book. It has survived not only five centuries, but also the leap into electronic typesetting, remaining essentially unchanged...</p>
    <span class="read-more">READ MORE</span>
    <div class="share">Share this :
      <span class="share-btn"><i style="background:#3b5998"></i>Friendly</span>
      <span class="share-btn"><i style="background:#2aa7de"></i>Chirper</span>
      <span class="share-btn"><i style="background:#d34836"></i>Searchly</span>
    </div>
    <div class="divider"></div>
  </article>

  <article class="post" style="top:712px">
    <h2 class="post-title">Philip Island Boat Scene</h2>
    <div class="meta">
      <span class="meta-item"><span class="meta-icon"><svg width="7" height="7" viewBox="0 0 10 10"><rect x="1" y="2" width="8" height="7" fill="none" stroke="#999"/><path d="M1 4.5h8" stroke="#999"/></svg></span>28<sup>th</sup>&nbsp;January 2014</span>
      <span class="meta-item"><span class="meta-icon"><svg width="7" height="7" viewBox="0 0 10 10"><ellipse cx="5" cy="4.5" rx="4" ry="3" fill="#999"/><path d="M3 7l-1 2 3-2" fill="#999"/></svg></span>10 comment</span>
      <span class="meta-item"><span class="meta-icon"><svg width="7" height="7" viewBox="0 0 10 10"><path d="M5 9L1.2 5A2.2 2.2 0 015 2.2 2.2 2.2 0 018.8 5z" fill="#999"/></svg></span>22 Likes</span>
    </div>
    <div class="post-image" style="background:linear-gradient(180deg,#6a9ad8 0%,#4a80d0 35%,#2a6ad8 55%,#1a5ad0 80%,#2a70e0 100%)" role="img" aria-label="Painting of two sailing boats on a calm blue bay"></div>
    <div class="stars">
      <svg width="10" height="10" viewBox="0 0 10 10"><path d="M5 .5l1.4 3 3.1.3-2.4 2.1.7 3.1L5 7.4 2.2 9l.7-3.1L.5 3.8l3.1-.3z" fill="#e8a11a"/></svg>
      <svg width="10" height="10" viewBox="0 0 10 10"><path d="M5 .5l1.4 3 3.1.3-2.4 2.1.7 3.1L5 7.4 2.2 9l.7-3.1L.5 3.8l3.1-.3z" fill="#e8a11a"/></svg>
      <svg width="10" height="10" viewBox="0 0 10 10"><path d="M5 .5l1.4 3 3.1.3-2.4 2.1.7 3.1L5 7.4 2.2 9l.7-3.1L.5 3.8l3.1-.3z" fill="#e8a11a"/></svg>
      <svg width="10" height="10" viewBox="0 0 10 10"><path d="M5 .5l1.4 3 3.1.3-2.4 2.1.7 3.1L5 7.4 2.2 9l.7-3.1L.5 3.8l3.1-.3z" fill="none" stroke="#999" stroke-width=".7"/></svg>
      <svg width="10" height="10" viewBox="0 0 10 10"><path d="M5 .5l1.4 3 3.1.3-2.4 2.1.7 3.1L5 7.4 2.2 9l.7-3.1L.5 3.8l3.1-.3z" fill="none" stroke="#999" stroke-width=".7"/></svg>
    </div>
    <p class="excerpt">Lorem Ipsum is simply dummy text of the printing and typesetting industry. Lorem Ipsum has been the industry's standard dummy text ever since the 1500s, when an unknown printer took a galley of type and scrambled it to make a type specimen book. It has survived not only five centuries, but also the leap into electronic typesetting, remaining essentially unchanged...</p>
    <span class="read-more">READ MORE</span>
    <div class="share">Share this :
      <span class="share-btn"><i style="background:#3b5998"></i>Friendly</span>
      <span class="share-btn"><i style="background:#2aa7de"></i>Chirper</span>
      <span class="share-btn"><i style="background:#d34836"></i>Searchly</span>
    </div>
    <div class="divider"></div>
  </article>

  <nav class="pager">
    <span>1</span><span>2</span><span>3</span>
    <span class="next"><svg width="9" height="6" viewBox="0 0 9 6"><path d="M0 3h7M5 .8L7.5 3 5 5.2" fill="none" stroke="#fff" stroke-width="1.2"/></svg></span>
  </nav>

  <h3 class="widget-title" style="left:24px">Follow Blog via E-mail</h3>
  <p class="follow-text">Enter your email address to follow this blog and receive notifications of new posts by email.</p>
  <div class="email-input">Enter your email ID</div>
  <span class="follow-btn">FOLLOW</span>

  <h3 class="widget-title" style="left:206px">Chirper Feeds</h3>
  <span class="feed-arrow" style="left:335px"><svg width="5" height="6" viewBox="0 0 5 6"><path d="M4 .5L1.3 3 4 5.5" fill="none" stroke="#fff" stroke-width="1.2"/></svg></span>
  <span class="feed-arrow" style="left:350px"><svg width="5" height="6" viewBox="0 0 5 6"><path d="M1 .5L3.7 3 1 5.5" fill="none" stroke="#fff" stroke-width="1.2"/></svg></span>
  <div class="feed-circle"></div>
  <div class="feed-box">Enter your email address to follow this blog <a>http://ca-tions of new</a> and receive</div>
  <div class="feed-author">DR.MARLOW <i></i></div>
</main>
</body>
</html>
```